Business Card Design for Mabel's Larder

We make food for dogs.
Business Card Design (using the logo designed by you). Our Brand color is a bright canary yellow. For example our signage is predominantly yellow, with the logo in black. I'd like the card also to use that imagery.
Feel free to use the two sides creatively.
Vertical Design is also great.

Industry/Entity Type

Pet food

Contact Information for Business Card

Name, email, website, phone no

Font styles to use
Sans Serif

Colors
59FF00
82FF00
B8FF75
E3FFCB
F4FFEA
FFF300
FFF600
FEFA6F
FFFEC7
FFFEE8

Requirements
Nice to have
• A graphic in the same brush stroke style of the logo shoeing a doggy bowl of food

```html
<!DOCTYPE html>
<html lang="en">
<head>
<meta charset="utf-8">
<title>Mabel's Larder — Business Card</title>
<link rel="stylesheet" href="https://fonts.googleapis.com/css2?family=Montserrat:wght@400;600;700&family=Roboto:wght@400&display=swap">
<style>
  :root {
    --backdrop-light: #e6e5e2;
    --backdrop-dark: #b3b2ae;
    --card-ink: #2a2a2a;
    --card-ink-deep: #1c1c1c;
    --canary: #fff300;
    --canary-line: #f5e53a;
    --paper-text: #f2f2f2;
  }
  * { box-sizing: border-box; margin: 0; padding: 0; }
  html, body { width: 1200px; height: 801px; overflow: hidden; }
  body {
    background: linear-gradient(160deg, var(--backdrop-light), var(--backdrop-dark));
    display: flex;
    align-items: center;
    justify-content: center;
    gap: 60px;
    font-family: "Roboto", Arial, sans-serif;
  }
  .card {
    position: relative;
    width: 525px;
    height: 300px;
    background: var(--card-ink);
    border-bottom: 4px solid var(--canary);
    border-left: 4px solid var(--canary);
    box-shadow: 0 14px 30px rgba(0,0,0,0.25);
    overflow: hidden;
  }
  .card-front .wordmark {
    position: absolute;
    top: 52px;
    right: 40px;
    display: flex;
    align-items: center;
    gap: 12px;
    font-family: "Montserrat", sans-serif;
    font-weight: 700;
    font-size: 30px;
    letter-spacing: 1px;
    text-transform: uppercase;
    color: var(--canary);
  }
  .wordmark-dot {
    width: 16px; height: 16px;
    border-radius: 50%;
    background: var(--canary);
  }
  .divider {
    position: absolute;
    left: 36px;
    right: 36px;
    top: 150px;
    height: 1px;
    background: var(--canary-line);
  }
  .person {
    position: absolute;
    left: 36px;
    top: 98px;
  }
  .person-name {
    font-family: "Montserrat", sans-serif;
    font-weight: 700;
    font-size: 21px;
    letter-spacing: 1px;
    text-transform: uppercase;
    color: var(--canary);
  }
  .person-role {
    font-size: 14px;
    color: var(--paper-text);
    margin-top: 2px;
  }
  .contact-list {
    position: absolute;
    left: 36px;
    top: 172px;
    list-style: none;
    font-size: 14px;
    line-height: 24px;
    color: var(--paper-text);
  }
  .contact-list li { display: flex; align-items: center; gap: 9px; }
  .contact-list svg { width: 13px; height: 13px; fill: var(--canary); flex: none; }
  .address {
    position: absolute;
    right: 36px;
    top: 172px;
    text-align: right;
    font-size: 14px;
    line-height: 22px;
    color: var(--paper-text);
  }
  .card-back {
    display: flex;
    align-items: center;
    justify-content: center;
  }
  .card-back .wordmark {
    display: flex;
    align-items: center;
    gap: 14px;
    font-family: "Montserrat", sans-serif;
    font-weight: 700;
    font-size: 40px;
    letter-spacing: 1px;
    text-transform: uppercase;
    color: var(--card-ink-deep);
  }
  .card-back .wordmark-dot { width: 20px; height: 20px; background: var(--card-ink-deep); }
</style>
</head>
<body>
  <section class="card card-front" aria-label="Card front">
    <div class="wordmark"><span class="wordmark-dot"></span>Mabel's Larder</div>
    <div class="person">
      <div class="person-name">Owen Carradine</div>
      <div class="person-role">Founder/CEO</div>
    </div>
    <div class="divider"></div>
    <ul class="contact-list">
      <li>
        <svg viewBox="0 0 24 24" aria-hidden="true"><path d="M6.6 10.8a15.1 15.1 0 0 0 6.6 6.6l2.2-2.2a1 1 0 0 1 1-.25 11.4 11.4 0 0 0 3.6.57 1 1 0 0 1 1 1V20a1 1 0 0 1-1 1A17 17 0 0 1 3 4a1 1 0 0 1 1-1h3.5a1 1 0 0 1 1 1c0 1.25.2 2.45.57 3.57a1 1 0 0 1-.25 1z"/></svg>
        (555)-204-3190
      </li>
      <li>
        <svg viewBox="0 0 24 24" aria-hidden="true"><path d="M2 5h20v14H2z M2 5l10 8 10-8" fill="var(--canary)"/><path d="M3 6l9 7 9-7" fill="none" stroke="#2a2a2a" stroke-width="1.6"/></svg>
        info@mabelslarder.com
      </li>
      <li>
        <svg viewBox="0 0 24 24" aria-hidden="true"><circle cx="12" cy="12" r="10"/><path d="M2 12h20M12 2c3 3 3 17 0 20M12 2c-3 3-3 17 0 20" fill="none" stroke="#2a2a2a" stroke-width="1.4"/></svg>
        www.mabelslarder.com
      </li>
    </ul>
    <div class="address">
      2190 Harbour Lane Road<br>
      Millbrook AB 5032
    </div>
  </section>

  <section class="card card-back" aria-label="Card back">
    <div class="wordmark"><span class="wordmark-dot"></span>Mabel's Larder</div>
  </section>
</body>
</html>
```